Wrenhollow Acres Organic Flower Farm, Farmer Florist

I am a flower grower and florist, so I do everything from the field to the vase. I want to include my website, phone, email and instagram

```html
<!DOCTYPE html>
<html lang="en">
<head>
<meta charset="utf-8">
<title>Wrenhollow Acres – Business Card</title>
<link rel="stylesheet" href="https://fonts.googleapis.com/css2?family=Arimo:wght@400&display=swap">
<style>
  :root {
    --bg: #e8e7e5;
    --paper: #fbfafa;
    --maroon: #5a1f26;
    --maroon-deep: #3f1519;
    --wine: #7a3540;
    --rose: #e8878a;
    --rose-edge: #d9767c;
    --emboss: #c98890;
    --sans: "Arimo", Arial, sans-serif;
  }
  * { margin: 0; padding: 0; box-sizing: border-box; }
  html, body { width: 1200px; height: 801px; overflow: hidden; }
  body {
    background: var(--bg);
    display: flex;
    align-items: center;
    justify-content: center;
    gap: 40px;
  }
  .card {
    position: relative;
    width: 540px;
    height: 310px;
    overflow: hidden;
    box-shadow: 0 6px 18px rgba(0,0,0,.14);
  }

  /* Front */
  .card--front {
    background: var(--paper);
    border-bottom: 6px solid var(--rose-edge);
  }
  .floral-art {
    position: absolute;
    left: 0; top: 0;
    width: 150px; height: 304px;
    background: linear-gradient(100deg, rgba(90,31,38,.55) 0%, rgba(90,31,38,.25) 60%, rgba(90,31,38,0) 100%);
  }
  .brand {
    position: absolute;
    right: 34px; top: 62px;
    display: flex;
    align-items: center;
    gap: 10px;
  }
  .brand__mark {
    width: 14px; height: 14px;
    border-radius: 50%;
    background: var(--maroon);
  }
  .brand__name {
    font-family: var(--sans);
    font-weight: 400;
    font-size: 26px;
    color: var(--maroon);
    line-height: 1;
  }
  .divider {
    position: absolute;
    left: 170px; right: 24px; top: 136px;
    height: 1.5px;
    background: var(--maroon);
  }
  .address {
    position: absolute;
    right: 34px; top: 150px;
    font-family: var(--sans);
    font-size: 13px;
    line-height: 1.3;
    color: var(--maroon);
  }
  .person {
    position: absolute;
    left: 170px; top: 150px;
  }
  .person__name {
    font-family: var(--sans);
    font-size: 17px;
    letter-spacing: .5px;
    color: var(--rose);
  }
  .person__role {
    font-family: var(--sans);
    font-size: 13px;
    color: var(--maroon);
    margin-top: 2px;
  }
  .person__rule {
    width: 190px;
    height: 1.5px;
    background: var(--maroon);
    margin: 8px 0;
  }
  .contacts { list-style: none; }
  .contacts li {
    display: flex;
    align-items: center;
    gap: 10px;
    font-family: var(--sans);
    font-size: 13.5px;
    color: var(--maroon);
    height: 22px;
  }
  .contacts svg { width: 13px; height: 13px; flex: none; }

  /* Back */
  .card--back {
    background: radial-gradient(ellipse at 60% 30%, var(--wine) 0%, var(--maroon) 55%, var(--maroon-deep) 100%);
    display: flex;
    align-items: center;
    justify-content: center;
    gap: 14px;
  }
  .back-brand__mark {
    width: 18px; height: 18px;
    border-radius: 50%;
    background: var(--emboss);
  }
  .back-brand__name {
    font-family: var(--sans);
    font-weight: 400;
    font-size: 34px;
    color: var(--emboss);
  }
</style>
</head>
<body>

  <section class="card card--front">
    <div class="floral-art" role="img" aria-label="Maroon wildflower stem illustration"></div>

    <div class="brand">
      <span class="brand__mark"></span>
      <span class="brand__name">Wrenhollow Acres</span>
    </div>

    <div class="divider"></div>

    <div class="address">Your address, city<br>state, ZIP 0000</div>

    <div class="person">
      <div class="person__name">MARLOW HAYES</div>
      <div class="person__role">Manager</div>
      <div class="person__rule"></div>
      <ul class="contacts">
        <li>
          <svg viewBox="0 0 16 16" aria-hidden="true"><path fill="var(--rose)" d="M3.5 1.5l2.5 0 1 3.5-1.6 1.2a8 8 0 0 0 4.4 4.4L11 9l3.5 1v2.5c0 1-1 2-2 2C6.8 14.5 1.5 9.2 1.5 3.5c0-1 1-2 2-2z"/></svg>
          555-014-2100
        </li>
        <li>
          <svg viewBox="0 0 16 16" aria-hidden="true"><rect x="1" y="3" width="14" height="10" fill="var(--rose)"/><path d="M1 3l7 6 7-6" fill="none" stroke="var(--paper)" stroke-width="1.3"/></svg>
          info@wrenhollow.com
        </li>
        <li>
          <svg viewBox="0 0 16 16" aria-hidden="true"><circle cx="8" cy="8" r="6.5" fill="none" stroke="var(--rose)" stroke-width="2"/><path d="M1.5 8h13M8 1.5c-3 3-3 10 0 13M8 1.5c3 3 3 10 0 13" fill="none" stroke="var(--rose)" stroke-width="1.2"/></svg>
          www.wrenhollow.com
        </li>
        <li>
          <svg viewBox="0 0 16 16" aria-hidden="true"><rect x="2" y="2" width="12" height="12" rx="2" fill="var(--rose)"/></svg>
          @wrenhollow
        </li>
      </ul>
    </div>
  </section>

  <section class="card card--back">
    <span class="back-brand__mark"></span>
    <span class="back-brand__name">Wrenhollow Acres</span>
  </section>

</body>
</html>
```